Eastvale Physiotherapy Website www.eastvalephysiotherapy.com.au

Create Wordpress website for Eastvale Physiotherapy which aligns with our other locations www.marrowbankphysiotherapy,com.au. We would like the website to present in a similar fashion to our exisiting site with similar headings and layout. We will then alter the text to make it location specific.

Coding

Coded - Design and coding required

Number of Pages Required

1 page

Font styles to use
Sans Serif

Requirements
Must have
• Colours of the website must match the colours of the colour Eastvale Physiotherapy logo
• Website must be complimentary to existing websites,
• www.marrowbankphysiotherapy.com.au
• www.marrowbankpilatesandrehab.com.au

```html
<!DOCTYPE html>
<html lang="en">
<head>
<meta charset="utf-8">
<title>Our Practitioners – Eastvale Physiotherapy</title>
<link href="https://fonts.googleapis.com/css2?family=Roboto:wght@400;500;700&family=Roboto+Condensed:wght@700&display=swap" rel="stylesheet">
<style>
:root{
  --navy:#262a5c;
  --navy-dark:#1c1f47;
  --text:#4a4a4a;
  --muted:#6b6b6b;
  --rule:#d9d9d9;
  --ring:#8c90b8;
  --footer-bg:#f1f1f1;
  --accent:#5aa7a0;
  --white:#ffffff;
}
*{box-sizing:border-box;margin:0;padding:0}
html,body{width:1200px;height:4327px;overflow:hidden}
body{font-family:"Roboto",sans-serif;color:var(--text);background:var(--white);position:relative}

/* header */
.site-header{position:absolute;top:0;left:0;width:1200px;height:118px;background:var(--white)}
.brand{position:absolute;left:92px;top:30px;display:flex;align-items:center;gap:12px}
.brand-dot{width:34px;height:34px;border-radius:50%;background:var(--navy)}
.brand-name{font-family:"Roboto",sans-serif;font-weight:700;font-size:26px;color:var(--navy);line-height:1.05;width:200px}
.callus{position:absolute;left:585px;top:22px;font-weight:700;font-size:19px;color:var(--navy);display:flex;align-items:center;gap:8px;letter-spacing:.5px}
.search{position:absolute;left:888px;top:18px;width:200px;height:32px;border:1px solid #ccc;border-radius:16px;font-size:13px;color:#999;padding:7px 14px}
.main-nav{position:absolute;right:70px;top:78px;display:flex;gap:30px;font-weight:500;font-size:17px;color:var(--navy);letter-spacing:.3px}

/* hero */
.hero{position:absolute;top:118px;left:0;width:1200px;height:472px;background:linear-gradient(180deg,#2a2a2a 0%,#3d3a36 45%,#1e1e1e 100%)}
.hero-title{position:absolute;top:158px;width:100%;text-align:center;font-family:"Roboto Condensed",sans-serif;font-weight:700;font-size:46px;color:var(--white);letter-spacing:1px}
.hero-text{position:absolute;top:240px;left:195px;width:810px;text-align:center;color:#e8e8e8;font-size:15px;line-height:1.6}

/* practitioners */
.practitioner{position:absolute;left:0;width:1200px;border-bottom:1px solid var(--rule)}
.practitioner:last-of-type{border-bottom:none}
.portrait{position:absolute;left:172px;width:236px;height:236px;border-radius:50%;border:3px solid var(--ring);padding:8px;background:var(--white)}
.portrait span{display:block;width:100%;height:100%;border-radius:50%;background:radial-gradient(circle at 50% 40%,#bdbdbd,#5a5a5a)}
.profile{position:absolute;left:490px;width:610px}
.name{font-family:"Roboto Condensed",sans-serif;font-weight:700;font-size:33px;color:var(--navy);letter-spacing:.5px}
.quals{font-weight:700;font-size:16px;color:var(--navy);margin:10px 0 22px}
.bio p{font-size:12.5px;line-height:1.75;color:var(--text);margin-bottom:16px}
.label{font-weight:700;font-size:13px;color:var(--navy);letter-spacing:.4px;text-transform:uppercase;margin-bottom:14px}
.memberships{position:absolute;left:95px;width:600px}
.memberships.in-profile{left:490px}
.memberships ul{list-style:none;font-size:13px;line-height:1.7;color:var(--text);columns:2;column-gap:20px}
.memberships ul.single{columns:1}
.bookings{position:absolute;left:95px;width:1010px}
.bookings .label{margin-bottom:8px}
.bookings .note{font-size:13px;color:var(--text)}
.book-btn{position:absolute;right:0;top:0;width:478px;height:46px;background:var(--navy);color:var(--white);font-size:14px;display:flex;align-items:center;justify-content:center;gap:8px;border-radius:4px}
.book-btn u{text-underline-offset:3px}

/* footer */
.site-footer{position:absolute;top:3912px;left:0;width:1200px;height:415px;background:var(--footer-bg)}
.footer-curve{position:absolute;top:-6px;left:0}
.footer-brand{position:absolute;left:88px;top:54px;display:flex;align-items:center;gap:10px}
.footer-brand .brand-name{font-size:20px;width:150px}
.footer-brand .brand-dot{width:26px;height:26px}
.social{position:absolute;left:128px;top:140px;display:flex;gap:10px}
.social span{width:30px;height:30px;border-radius:50%;border:2px solid var(--navy)}
.footer-col{position:absolute;top:44px}
.footer-col h3{font-weight:700;font-size:22px;color:var(--navy);letter-spacing:.5px;margin-bottom:22px}
.contact{left:326px;width:290px}
.contact li{list-style:none;display:flex;gap:10px;font-size:13px;line-height:1.5;color:var(--text);margin-bottom:14px}
.contact svg{flex:none;margin-top:2px}
.newsletter{left:648px;width:270px}
.newsletter p{font-size:12px;line-height:1.5;color:var(--muted);margin-bottom:14px}
.newsletter .field{width:240px;height:36px;border:1px solid #ccc;background:var(--white);font-size:12px;color:#999;padding:10px}
.newsletter .submit{margin-top:14px;width:110px;height:36px;background:var(--navy);color:var(--white);font-weight:700;font-size:12px;display:flex;align-items:center;justify-content:center}
.quick{left:978px;width:180px}
.quick li{list-style:none;font-size:13px;color:var(--text);line-height:1.75;padding-left:16px;position:relative}
.quick li::before{content:"";position:absolute;left:2px;top:9px;width:5px;height:5px;background:var(--navy)}
.copyright{position:absolute;bottom:0;left:0;width:100%;height:40px;border-top:1px solid var(--rule);text-align:center;font-size:12px;color:var(--muted);line-height:40px}
</style>
</head>
<body>

<header class="site-header">
  <div class="brand"><span class="brand-dot"></span><span class="brand-name">Eastvale Physiotherapy</span></div>
  <div class="callus">
    <svg width="18" height="18" viewBox="0 0 24 24"><path fill="#262a5c" d="M6.6 10.8a15.1 15.1 0 0 0 6.6 6.6l2.2-2.2c.3-.3.7-.4 1-.2 1.1.4 2.3.6 3.6.6.6 0 1 .4 1 1V20c0 .6-.4 1-1 1A17 17 0 0 1 3 4c0-.6.4-1 1-1h3.5c.6 0 1 .4 1 1 0 1.3.2 2.5.6 3.6.1.3 0 .7-.2 1z"/></svg>
    CALLUS : 03 9000 4412
  </div>
  <div class="search">Search here</div>
  <nav class="main-nav"><span>HOME</span><span>ABOUT</span><span>SERVICES</span><span>CONDITIONS</span><span>HEALTH TIPS</span><span>BLOG</span><span>CONTACT</span></nav>
</header>

<section class="hero" role="img" aria-label="Dark photograph of a runner on a tree-lined path">
  <h1 class="hero-title">OUR PRACTITIONERS</h1>
  <p class="hero-text">All practitioners at our clinic have completed or are completing postgraduate university training and most are involved in teaching, university lecturing and research. This means that you are being treated by highly qualified people at the forefront of new developments in the management of musculoskeletal disorders.</p>
</section>

<!-- Practitioner 1 -->
<article class="practitioner" style="top:620px;height:710px">
  <div class="portrait" style="top:40px" role="img" aria-label="Portrait photo of Harriet Lowell"><span></span></div>
  <div class="profile" style="top:62px">
    <h2 class="name">DR HARRIET LOWELL</h2>
    <p class="quals">B App Sc (Physio) Grad Dip (Manip Physio) PhD (Director)</p>
    <div class="bio">
      <p>Harriet is a highly experienced Musculoskeletal Physiotherapist and Associate Professor at Southbridge University. She is a founding director of Marrowbank Physiotherapy and Marrowbank Pilates and Rehab. She is recognised as a leading clinician, researcher and educator in the diagnosis and management of anterior knee pain. Harriet also has a particular interest in spinal pain and has post graduate qualifications in Manipulative Physiotherapy. In addition she has many years experience working with sporting teams and athletes.</p>
      <p>Harriet is a regular lecturer and supervisor to post graduate physiotherapy students at Southbridge University. She has over 50 publications in international peer reviewed journals and has co-authored four book chapters on anterior knee pain and one on core stability, including in the most popular sports medicine text of all time. Harriet has been invited to speak both nationally and internationally on the topic of knee pain, and has received numerous awards for her research.</p>
    </div>
  </div>
  <div class="memberships" style="top:462px">
    <h3 class="label">Professional Memberships</h3>
    <ul class="single"><li>National Physiotherapy Council Titled member of Musculoskeletal Physiotherapy</li><li>Sports Health Network</li><li>Dr Harriet Lowell Publications – HLowell Publications</li></ul>
  </div>
  <div class="bookings" style="top:563px">
    <h3 class="label">Bookings</h3>
    <p class="note">ONLINE &nbsp;Not available for online bookings</p>
    <div class="book-btn">CALL &nbsp;<u>Contact us for an appointment with &nbsp;Harriet Lowell</u></div>
  </div>
</article>

<!-- Practitioner 2 -->
<article class="practitioner" style="top:1330px;height:630px">
  <div class="portrait" style="top:36px" role="img" aria-label="Portrait photo of Miriam Ashdown"><span></span></div>
  <div class="profile" style="top:58px">
    <h2 class="name">MIRIAM ASHDOWN</h2>
    <p class="quals">B App Sc (Physio) Post Grad Cert Physio (Continence &amp; Women's Health) &nbsp;(Director)</p>
    <div class="bio">
      <p>Miriam is an experienced physiotherapist with post graduate qualifications in Continence and Pelvic Floor Rehabilitation from Southbridge University and Post Graduate studies in Pain Management from Harbourside University. Miriam is a founding Director of Marrowbank Physiotherapy and Marrowbank Pilates &amp; Rehab. Miriam is a regular clinical supervisor and lecturer to postgraduate students and has a special interest in women's and men's pelvic health, particularly persistent pelvic pain and continence.</p>
      <p>Miriam has extensive experience working in hospitals and private practice at home and overseas. She has worked for many years managing sporting, spinal and musculoskeletal conditions. Having worked 15 years as senior clinician in a continence clinic, Miriam understands the impact of bladder and bowel dysfunction on men, women and children. She has also worked in a multidisciplinary pain clinic and has a specific interest in neuroscience education in chronic pain and a passion for the management of persistent pelvic pain.</p>
    </div>
  </div>
  <div class="memberships" style="top:372px">
    <h3 class="label">Professional Memberships</h3>
    <ul><li>National Physiotherapy Council</li><li>Chronic Pain Society</li><li>Pelvic Pain Alliance</li><li>Pelvic Health Foundation</li><li>Continence &amp; Women's Health Group NPC</li></ul>
  </div>
  <div class="bookings" style="top:540px">
    <h3 class="label">Bookings</h3>
    <p class="note">ONLINE &nbsp;Not available for online bookings</p>
    <div class="book-btn">CALL &nbsp;<u>Contact us for an appointment with Miriam Ashdown</u></div>
  </div>
</article>

<!-- Practitioner 3 -->
<article class="practitioner" style="top:1960px;height:605px">
  <div class="portrait" style="top:44px" role="img" aria-label="Portrait photo of Claire Penhallow"><span></span></div>
  <div class="profile" style="top:72px">
    <h2 class="name">CLAIRE PENHALLOW</h2>
    <p class="quals">B Physio Post Grad Cert Physio (Continence &amp; Women's Health) (Director)</p>
    <div class="bio">
      <p>Claire completed her Bachelor of physiotherapy at Southbridge University in 2009 and more recently her Grade Cert in Pelvic Floor and Womens Health. Since graduating she has travelled and worked extensively through the region and overseas in both public hospitals and private practice.</p>
      <p>Claire has been working with football and netball teams and dancers in both injury prevention and management and has a keen interest in helping people of all levels to achieve their maximum function.</p>
      <p>She uses a combined musculoskeletal, exercise prescription and clinical pilates approach in her treatment. She has a special interest in chronic pelvic pain, neurological and vestibular rehabilitation.</p>
    </div>
  </div>
  <div class="memberships in-profile" style="top:396px">
    <h3 class="label">Professional Memberships</h3>
    <ul class="single"><li>National Physiotherapy Council</li></ul>
  </div>
  <div class="bookings" style="top:492px">
    <h3 class="label">Bookings</h3>
    <p class="note">ONLINE &nbsp;Not available for online bookings</p>
    <div class="book-btn">CALL &nbsp;<u>Contact us for an appointment with Claire Penhallow</u></div>
  </div>
</article>

<!-- Practitioner 4 -->
<article class="practitioner" style="top:2565px;height:650px">
  <div class="portrait" style="top:36px" role="img" aria-label="Portrait photo of Tobias Renwick"><span></span></div>
  <div class="profile" style="top:60px">
    <h2 class="name">TOBIAS RENWICK</h2>
    <p class="quals">B Pod M Physio</p>
    <div class="bio">
      <p>Tobias is a Physiotherapist with over 12 years experience in private practice. He graduated from Westmoor University with a Master of Physiotherapy (Graduate Entry) in 2005 after previously completing a Bachelor of Podiatry in 2001.</p>
      <p>Tobias incorporates a distinct focus on manual and exercise therapy and holistic care, placing great emphasis on having his clients be an active participant in their therapy to optimise their treatment outcomes.</p>
      <p>Tobias has undertaken further training in the fields of Craniosacral Therapy and Visceral Manipulation which looks to address correction of connective tissue restrictions throughout the body and the implications they have on dysfunction of the musculo-skeletal, nervous, vascular, cardio-respiratory, digestive and endocrine systems.</p>
      <p>Tobias's special interest areas include pelvic and spinal disorders, lower limb problems due to his background in Podiatry, headaches and migraines, jaw problems and chronic pain syndromes.</p>
      <p>In his spare time Tobias is an avid music collector, movie watcher and Riverside Hawks supporter.</p>
    </div>
  </div>
  <div class="memberships" style="top:508px">
    <h3 class="label">Professional Memberships</h3>
    <ul class="single"><li>National Physiotherapy Council</li></ul>
  </div>
  <div class="bookings" style="top:580px">
    <h3 class="label">Bookings</h3>
    <p class="note">ONLINE</p>
    <div class="book-btn">CALL &nbsp;<u>to make an appointment with Tobias</u></div>
  </div>
</article>

<!-- Practitioner 5 -->
<article class="practitioner" style="top:3215px;height:660px">
  <div class="portrait" style="top:36px" role="img" aria-label="Portrait photo of Declan Morrow"><span></span></div>
  <div class="profile" style="top:60px">
    <h2 class="name">DECLAN MORROW</h2>
    <p class="quals">Nemo enim ipsam voluptatem quia voluptas sit</p>
    <div class="bio">
      <p>Sed ut perspiciatis unde omnis iste natus error sit voluptatem accusantium doloremque laudantium, totam rem aperiam, eaque ipsa quae ab illo inventore veritatis et quasi architecto beatae vitae dicta sunt explicabo. Nemo enim ipsam voluptatem quia voluptas sit aspernatur aut odit aut fugit, sed quia consequuntur magni dolores eos qui ratione voluptatem sequi nesciunt.</p>
      <p>Neque porro quisquam est, qui dolorem ipsum quia dolor sit amet, consectetur, adipisci velit, sed quia non numquam eius modi tempora incidunt ut labore et dolore magnam aliquam quaerat voluptatem. Ut enim ad minima veniam, quis nostrum exercitationem ullam corporis suscipit laboriosam, nisi ut aliquid ex ea commodi consequatur? Quis autem vel eum iure reprehenderit qui in ea voluptate velit esse quam nihil molestiae consequatur, vel illum qui dolorem eum fugiat quo voluptas nulla pariatur?</p>
    </div>
  </div>
  <div class="memberships in-profile" style="top:464px">
    <h3 class="label">Professional Memberships</h3>
    <ul class="single"><li>Nemo enim ipsam voluptatem quia voluptas sit</li></ul>
  </div>
  <div class="bookings" style="top:590px">
    <h3 class="label">Bookings</h3>
    <p class="note">ONLINE</p>
    <div class="book-btn">CALL &nbsp;<u>to make an appointment with Declan Morrow</u></div>
  </div>
</article>

<footer class="site-footer">
  <svg class="footer-curve" width="1200" height="30" viewBox="0 0 1200 30"><path d="M0 22 Q600 -8 1200 22" fill="none" stroke="#5aa7a0" stroke-width="2"/></svg>
  <div class="footer-brand"><span class="brand-dot"></span><span class="brand-name">Eastvale Physiotherapy</span></div>
  <div class="social"><span></span><span></span></div>

  <div class="footer-col contact">
    <h3>CONTACT US</h3>
    <ul>
      <li><svg width="14" height="16" viewBox="0 0 24 24"><path fill="#262a5c" d="M12 2a7 7 0 0 0-7 7c0 5 7 13 7 13s7-8 7-13a7 7 0 0 0-7-7zm0 9.5A2.5 2.5 0 1 1 12 6.5a2.5 2.5 0 0 1 0 5z"/></svg><span>Eastvale Physiotherapy 118 Orchard Road, Eastvale, VIC 3999</span></li>
      <li><svg width="14" height="14" viewBox="0 0 24 24"><path fill="#262a5c" d="M6.6 10.8a15.1 15.1 0 0 0 6.6 6.6l2.2-2.2c.3-.3.7-.4 1-.2 1.1.4 2.3.6 3.6.6.6 0 1 .4 1 1V20c0 .6-.4 1-1 1A17 17 0 0 1 3 4c0-.6.4-1 1-1h3.5c.6 0 1 .4 1 1 0 1.3.2 2.5.6 3.6.1.3 0 .7-.2 1z"/></svg><span>Phone: 1-800-555-0192</span></li>
      <li><svg width="14" height="14" viewBox="0 0 24 24"><path fill="#262a5c" d="M3 5h18v14H3zm2 2v.5l7 4.5 7-4.5V7l-7 4.5z"/></svg><span>hello@eastvalephysiotherapy.com.au</span></li>
    </ul>
  </div>

  <div class="footer-col newsletter">
    <h3>SIGN UP FOR NEWSLETTER</h3>
    <p>Excepteur sint occaecat cupidatat non proident, sunt in culpa qui officia deserunt</p>
    <div class="field">Enter email</div>
    <div class="submit">SUBSCRIPTION</div>
  </div>

  <div class="footer-col quick">
    <h3>QUICK LINKS</h3>
    <ul><li>Home</li><li>About</li><li>Service</li><li>Conditions</li><li>Health Tips</li><li>Blog</li><li>Contact Us</li></ul>
  </div>

  <div class="copyright">©2018 Eastvale Physiotherapy, All Rights Reserved.</div>
</footer>

</body>
</html>
```